New Book Cover Design Project for The Lantern Hopper

I need a book cover designed for my book, "9 Bright Paths to Steady Wealth on Your Terms, Leave the Office Grind, and Chase Your Horizon!" The cover needs to include my logo. It's a step by step guide to earning money from home in various different ways. By doing this, people can quit their jobs and live their dream life. A life with purpose, happiness and abundance. I would love an image of a lady in a suit crushing a desk, or of someone sitting on a island or of money abundantly flowing or a combination of all of these things. It needs to represent the dream life and be visually strong to look at. It needs to include the logo at the top. Its important that people identify with it instantly.

Project Deadline Extended Reason: I've extended the deadline as I realised I not provided some key details such as dimensions of the book, author's name plus details for the back cover. Thanks. Added Sunday, August 6, 2017

Target Market(s)

Women over 30 who are fed up with working in a cubicle and of corporate life.

Industry/Entity Type

Entrepreneur

Font styles to use
Other font styles liked:
• Arial Narrow or Century Gothic or something fun!

Colors

Designer to choose colors to be used in the design.

Requirements
Must have
• My logo at the top (non-negotiable). It needs to convey someone living their dreams or quitting their job or crushing their cubicle. I want it to be like no other title. Visually strong, clear and representative of what it is about. This book represents an opportunity for people to transform their lives! I want them to see this book and want to buy it.
Nice to have
• Examples could be leaving their desk and entering through a door to an amazing life. Money could feature somewhere in it. It needs to represent the dream and someone attaining it. It could feature balloons to escape their desk, or climbing out of their desk to an amazing life.
Should not have
• Anything scary! I don't want too many images or confusing images.

```html
<!DOCTYPE html>
<html lang="en">
<head>
<meta charset="utf-8">
<title>The Lantern Hopper – Book Cover</title>
<link href="https://fonts.googleapis.com/css2?family=Archivo+Black&family=Montserrat:wght@500&display=swap" rel="stylesheet">
<style>
  :root {
    --teal: #5bb1b7;
    --teal-soft: #d7ecee;
    --slate: #6b6c6f;
    --slate-soft: #c9cacc;
    --paper: #ffffff;
    --backdrop: #303032;
  }
  html, body {
    margin: 0;
    width: 1200px;
    height: 1114px;
    overflow: hidden;
    background: var(--backdrop);
  }
  .cover {
    position: absolute;
    left: 250px;
    top: 97px;
    width: 700px;
    height: 920px;
    background: var(--paper);
    overflow: hidden;
  }
  .band {
    position: absolute;
    top: 0;
    bottom: 0;
    background: var(--teal);
  }
  .band--left { left: 22px; width: 72px; }
  .band--right { right: 22px; width: 72px; }

  .brand {
    position: absolute;
    left: 132px;
    top: 60px;
    width: 450px;
    display: flex;
    align-items: center;
    gap: 16px;
  }
  .brand__mark {
    flex: none;
    width: 54px;
    height: 54px;
    background: var(--slate);
  }
  .brand__name {
    font-family: "Montserrat", "Century Gothic", sans-serif;
    font-weight: 500;
    font-size: 32px;
    line-height: 1;
    white-space: nowrap;
    color: var(--teal);
  }

  .title {
    position: absolute;
    left: 132px;
    top: 170px;
    width: 450px;
    margin: 0;
    font-family: "Archivo Black", "Arial Black", sans-serif;
    font-weight: 400;
    text-transform: uppercase;
    line-height: 0.9;
  }
  .title .row { display: flex; align-items: center; gap: 10px; }
  .title .stack { display: flex; flex-direction: column; gap: 4px; }
  .title .small { font-size: 26px; color: var(--slate); }
  .title .tiny { font-size: 20px; color: var(--slate); }
  .title .big-num { font-size: 150px; color: var(--teal); line-height: 0.8; }
  .title .mid-num { font-size: 64px; color: var(--teal); }
  .title .hero { font-size: 84px; color: var(--teal); letter-spacing: -3px; display: block; margin: 6px 0; }
  .title .hero--end { font-size: 74px; }

  .doorway-art {
    position: absolute;
    left: 132px;
    top: 640px;
    width: 450px;
    height: 240px;
    background: linear-gradient(135deg, var(--teal-soft) 0%, var(--slate-soft) 100%);
  }
</style>
</head>
<body>
  <main class="cover">
    <div class="band band--left"></div>
    <div class="band band--right"></div>

    <header class="brand">
      <div class="brand__mark"></div>
      <span class="brand__name">The Lantern Hopper</span>
    </header>

    <h1 class="title">
      <span class="row">
        <span class="big-num">9</span>
        <span class="stack">
          <span class="small">Bright</span>
          <span class="small">Paths</span>
          <span class="tiny">to Steady</span>
        </span>
      </span>
      <span class="hero">Wealth</span>
      <span class="row">
        <span class="stack">
          <span class="tiny">On Your</span>
          <span class="tiny">Terms,</span>
        </span>
        <span class="mid-num">&amp;</span>
        <span class="stack">
          <span class="tiny">Leave the Office</span>
          <span class="tiny">Grind and Chase Your</span>
        </span>
      </span>
      <span class="hero hero--end">Horizon!</span>
    </h1>

    <div class="doorway-art" role="img" aria-label="Illustration of open double doors revealing a large dollar sign, with small dollar signs floating around"></div>
  </main>
</body>
</html>
```